Luxury Photoalbum manufacturer needs banner design 8'x8'

We need a banner design for trade show purposes. We supply luxury one-of-a-kind photo albums to boudoir photographers. Our customers are female professional photographers - mostly in the age range of 26 - 40.Design needs to appeal to business women in this age range who see their business help empower women.Follow our website for our current look and feel. www.velvetkeepsake.com
It needs to be 8'x8'

Target Market(s)

Women professional boudoir photographers

Industry/Entity Type

Professional Photography

Font styles to use
Serif

Requirements
Must have
• Feminine but professional look and feel
• Need the LOGO to be very dominant
• Needs to be reasonably consistent with our website - www.velvetkeepsake.com
Nice to have
• Not necessary to use all the images - can use as few or many as makes sense.

```html
<!DOCTYPE html>
<html lang="en">
<head>
<meta charset="utf-8">
<title>Velvet Keepsake – Trade Show Banner</title>
<link rel="stylesheet" href="https://fonts.googleapis.com/css2?family=Bebas+Neue&family=Yellowtail&display=swap">
<style>
  :root {
    --violet-core: #5a2f72;
    --violet-mid: #3e2250;
    --charcoal-edge: #222024;
    --frame-violet: #7d55ad;
    --ink-white: #ffffff;
  }
  html, body {
    margin: 0;
    padding: 0;
    width: 1200px;
    height: 1200px;
    overflow: hidden;
    background: var(--charcoal-edge);
  }
  .banner {
    position: relative;
    width: 1200px;
    height: 1200px;
    overflow: hidden;
    background:
      radial-gradient(ellipse 62% 58% at 50% 46%, var(--violet-core) 0%, var(--violet-mid) 55%, var(--charcoal-edge) 100%);
  }
  .brand-name {
    position: absolute;
    top: 120px;
    left: 0;
    width: 100%;
    margin: 0;
    text-align: center;
    font-family: "Bebas Neue", sans-serif;
    font-weight: 400;
    font-size: 150px;
    line-height: 1;
    letter-spacing: 4px;
    color: var(--ink-white);
  }
  .tagline {
    position: absolute;
    top: 425px;
    left: 0;
    width: 100%;
    margin: 0;
    text-align: center;
    color: var(--ink-white);
    font-family: "Bebas Neue", sans-serif;
    font-weight: 400;
    font-size: 64px;
    line-height: 62px;
  }
  .tagline .line { display: block; }
  .tagline .line-one { transform: translateX(-12px); }
  .tagline .line-two { transform: translateX(-10px); }
  .tagline .script {
    font-family: "Yellowtail", cursive;
    font-size: 66px;
    letter-spacing: 0;
  }
  .album-photo {
    position: absolute;
    width: 383px;
    height: 255px;
    box-sizing: border-box;
    border: 9px solid var(--frame-violet);
  }
  .photo-jewel-stack { left: 202px; top: 571px;
    background: linear-gradient(160deg, #5c3a52 0%, #9c1e32 40%, #6e5b50 60%, #7d1426 78%, #2a2426 100%); }
  .photo-ivory-ribbon { left: 612px; top: 571px;
    background: linear-gradient(170deg, #9a9a9c 0%, #dcd8d4 42%, #c9b7bd 55%, #5d6380 78%, #4a4c5a 100%); }
  .photo-silver-stack { left: 202px; top: 866px;
    background: linear-gradient(165deg, #7b7d80 0%, #b8bbbb 30%, #8e9091 55%, #4a4b4e 80%, #2c2c2e 100%); }
  .photo-ruby-navy { left: 612px; top: 866px;
    background: linear-gradient(170deg, #6f6c66 0%, #c3b9a4 22%, #8e1b2c 45%, #1f2448 70%, #141418 100%); }
</style>
</head>
<body>
  <main class="banner">
    <h1 class="brand-name">Velvet Keepsake</h1>

    <p class="tagline">
      <span class="line line-one"><span class="script">Time</span> is not measured by clock</span>
      <span class="line line-two">but by <span class="script">Moments...</span></span>
    </p>

    <div class="album-photo photo-jewel-stack" role="img" aria-label="Stack of jewel-toned velvet albums in purple, red and bronze draped with pearl strands"></div>
    <div class="album-photo photo-ivory-ribbon" role="img" aria-label="Ivory and slate-blue albums tied with a pale pink satin ribbon and pearls"></div>
    <div class="album-photo photo-silver-stack" role="img" aria-label="Stack of silver and grey albums with white satin ribbon on silver fabric"></div>
    <div class="album-photo photo-ruby-navy" role="img" aria-label="Stack of albums with gold lace, ruby, navy and black covers"></div>
  </main>
</body>
</html>
```